Redesign retirement planner website

Provide an original design for a website. The site should introduce the retirement planner, explain the basic offerings of his services, and invite the website visitor to enter their name, phone, and email. Please provide a ready-to-publish redesign that can actually be published via a Wordpress template or other major website builder like SquareSpace or Wix. Some introductory content is attached, but feel free to add additional sections/images/blocks/copywriting and rearrange/delete sections entirely to make your design original and compelling. Feel free to pull copywriting from here but again, do not use this original design, feel free to create an entirely NEW design and layout. tern-melon-zobr (dot) sitelarkhost (dot) com password: 1234 -- FINAL NOTE: Do not choose a stock photo of a man for the retirement planner. This website needs to work well with no photo of the retirement planner himself. Think of a non-face-focused design to win this competition.

Industry/Entity Type

Retirement planner personal website

Number of Pages Required

1 page

Font styles to use
Sans Serif
Decorative

Requirements
Must have
• Please provide a ready-to-publish redesign that can actually be published via a Wordpress template or other major website builder.

```html
<!DOCTYPE html>
<html lang="en">
<head>
<meta charset="utf-8">
<title>Daniel Marrow — Retirement Planning</title>
<link href="https://fonts.googleapis.com/css2?family=Plus+Jakarta+Sans:wght@400;500;600;700;800&family=Playfair+Display:wght@400;500&display=swap" rel="stylesheet">
<style>
:root{
  --yellow:#f5bd00;
  --yellow-soft:#f9cc2e;
  --dark:#2a2a2a;
  --darker:#1d1d1d;
  --panel:#3a3a3a;
  --white:#ffffff;
  --muted:#b9b9b9;
  --line:#5a5a5a;
  --ink:#141414;
  --card-text:#4a4a4a;
}
*{box-sizing:border-box;margin:0;padding:0}
html,body{width:1200px;height:3131px;overflow:hidden}
body{font-family:"Plus Jakarta Sans",Arial,sans-serif;background:var(--dark);color:var(--white);position:relative}
.abs{position:absolute}
.serif{font-family:"Playfair Display",Georgia,serif;font-weight:400}
.eyebrow{color:var(--yellow);font-size:13px;font-weight:700;letter-spacing:1.2px;text-transform:uppercase}
.btn{display:flex;align-items:center;justify-content:center;border-radius:30px;font-size:13px;font-weight:700}
.btn-yellow{background:var(--yellow);color:var(--ink)}

/* hero */
.hero{left:0;top:0;width:1200px;height:659px;
  background:linear-gradient(90deg,rgba(40,28,20,.85) 0%,rgba(60,40,28,.55) 45%,rgba(0,0,0,0) 75%),
  linear-gradient(135deg,#8a7464 0%,#b7a494 35%,#6d4638 55%,#2f3a52 75%,#c9bfb4 100%)}
.logo{font-weight:700;font-size:22px;color:var(--yellow)}
.nav a{color:var(--white);font-size:15px;font-weight:600;text-decoration:none;position:absolute}
.hero-kicker{left:85px;top:182px;font-size:17px;font-weight:700}
.hero-title{left:85px;top:208px;width:470px;font-size:36px;line-height:45px;font-weight:700}
.slider-num{font-size:12px;font-weight:700}

/* about */
.about-photo{left:85px;top:779px;width:456px;height:397px;border-radius:12px;
  background:linear-gradient(120deg,#d9d4cf 0%,#f4f1ee 45%,#e6dfe4 70%,#c9ccd2 100%);z-index:2}
.about-back{left:515px;top:797px;width:46px;height:379px;background:var(--yellow);border-radius:0 14px 14px 0}
.about-name{left:613px;top:852px;font-size:52px}
.about-text{left:613px;top:932px;width:505px;font-size:17.2px;line-height:33px;color:#e4e4e4}

.divider{left:85px;width:1030px;height:1px;background:var(--line)}

/* specialties */
.spec-title{left:83px;top:1440px;font-size:44px;line-height:48px}
.card{top:1577px;width:245px;height:250px;border-radius:10px;background:var(--white);color:var(--ink);padding:16px 17px;border:2px solid #e8e8e8}
.card.active{background:var(--yellow);border-color:var(--yellow);color:var(--white);box-shadow:0 16px 30px rgba(0,0,0,.35)}
.card-icon{width:44px;height:44px;border-radius:8px}
.card h3{font-size:16px;font-weight:700;margin-top:17px}
.card p{font-size:13.5px;line-height:23px;color:var(--card-text);margin-top:6px;height:92px;overflow:hidden}
.card.active p{color:var(--white)}
.card .more{display:inline-flex;gap:8px;margin-top:17px;font-size:12px;font-weight:800;letter-spacing:1.4px;border-bottom:1px solid currentColor;padding-bottom:2px}

/* contact */
.contact-panel{left:85px;top:2053px;width:530px;height:479px;background:var(--panel);border-radius:12px 0 0 12px}
.contact-photo{left:613px;top:2053px;width:502px;height:479px;border-radius:0 12px 12px 0;
  background:linear-gradient(160deg,#6a5140 0%,#9a8877 35%,#7f9ec6 60%,#a9c1de 80%,#d8d4cc 100%)}
.contact-title{left:121px;top:2116px;font-size:49px;line-height:52px}
.field{height:42px;background:var(--white);color:#555;font-size:14px;padding:0 13px;display:flex;align-items:center;border-radius:2px}

/* footer */
.footer-bg{left:0;top:2634px;width:1200px;height:497px;background:var(--darker)}
.cta{left:184px;top:2577px;width:832px;height:159px;background:var(--yellow);border-radius:14px;overflow:hidden}
.cta-tint{right:0;top:0;width:170px;height:159px;background:linear-gradient(90deg,rgba(249,204,46,0) 0%,var(--yellow-soft) 100%)}
.cta-title{left:55px;top:22px;font-size:48px;line-height:54px;color:var(--white)}
.col-head{font-size:14px;color:var(--muted)}
.col-link{font-size:14px;font-weight:700;color:var(--white)}
</style>
</head>
<body>

<!-- hero -->
<section class="abs hero" role="img" aria-label="Photo of a senior couple reviewing retirement plans on a laptop in a bright living room"></section>
<div class="abs logo" style="left:85px;top:26px">Daniel Marrow</div>
<nav class="nav">
  <a style="left:770px;top:32px">Home</a>
  <a style="left:848px;top:32px">Specialties</a>
</nav>
<div class="abs btn btn-yellow" style="left:961px;top:19px;width:154px;height:44px">Contact Me</div>
<div class="abs hero-kicker">I’m a</div>
<h1 class="abs hero-title">Counselor &amp; Retirement Specialist with a unique approach to Financial planning</h1>
<div class="abs btn btn-yellow" style="left:85px;top:424px;width:215px;height:44px">Explore Retirement Plans</div>
<div class="abs slider-num" style="left:87px;top:588px;color:var(--yellow)">01</div>
<div class="abs slider-num" style="left:208px;top:588px">04</div>
<div class="abs" style="left:85px;top:608px;width:138px;height:1px;background:#8a8a8a"></div>
<div class="abs" style="left:85px;top:607px;width:20px;height:2px;background:var(--yellow)"></div>

<!-- about -->
<div class="abs about-back"></div>
<div class="abs about-photo" role="img" aria-label="Photo of a senior couple smiling at a desk while signing documents"></div>
<div class="abs eyebrow" style="left:613px;top:840px">About</div>
<h2 class="abs serif about-name">Daniel Marrow</h2>
<p class="abs about-text">You have a lifetime of accomplishments. Learning about them is my extraordinary honor. When I meet clients to make a plan for their final years of work and savings, I understand my solemn privilege. Your capital is irreplaceable. My job is to maximize its benefit for your health, family, and legacy.</p>
<div class="abs divider" style="top:1314px"></div>

<!-- specialties -->
<div class="abs eyebrow" style="left:83px;top:1421px">My Specialties</div>
<h2 class="abs serif spec-title">Retirement<br>Planning Services</h2>
<div class="abs btn btn-yellow" style="left:968px;top:1465px;width:147px;height:45px">View All</div>

<article class="abs card" style="left:85px">
  <div class="card-icon" style="background:linear-gradient(135deg,#f2d06b,#e04f3f)" role="img" aria-label="Estate documents icon"></div>
  <h3>Estate Planning</h3>
  <p>Ensure your legacy is protected with comprehensive estate planning. I will guide you through creating wills, trusts</p>
  <span class="more">READ MORE <span>→</span></span>
</article>
<article class="abs card active" style="left:347px">
  <div class="card-icon" style="background:linear-gradient(135deg,#ffe08a,#d98a1c)" role="img" aria-label="Retirement chart icon"></div>
  <h3>Retirement forecasting</h3>
  <p>Plan for a fulfilling retirement with our expert forecasting services. I will analyze your financial situation and future</p>
  <span class="more">READ MORE <span>→</span></span>
</article>
<article class="abs card" style="left:609px">
  <div class="card-icon" style="background:linear-gradient(135deg,#f5a623,#d2452e)" role="img" aria-label="Expense coin icon"></div>
  <h3>Final Expense</h3>
  <p>Prepare for life’s final expenses with peace of mind. My services help you plan for costs associated with</p>
  <span class="more">READ MORE <span>→</span></span>
</article>
<article class="abs card" style="left:871px">
  <div class="card-icon" style="background:linear-gradient(135deg,#4fc3e8,#2b3a55)" role="img" aria-label="Family umbrella icon"></div>
  <h3>Life insurance</h3>
  <p>Safeguard your family’s future with tailored life insurance solutions. I provide expert advice to help you</p>
  <span class="more">READ MORE <span>→</span></span>
</article>

<div class="abs divider" style="top:1976px"></div>

<!-- contact -->
<div class="abs contact-panel"></div>
<div class="abs contact-photo" role="img" aria-label="Photo of a smiling senior advisor seated in front of bookshelves"></div>
<div class="abs eyebrow" style="left:121px;top:2098px">Contact Me</div>
<h2 class="abs serif contact-title">Allow me to<br>introduce myself</h2>
<div class="abs" style="left:119px;top:2231px;font-size:14px;font-weight:500">(Let’s plan for golden memories.)</div>
<div class="abs field" style="left:120px;top:2280px;width:229px">First Name</div>
<div class="abs field" style="left:358px;top:2280px;width:229px">Last Name</div>
<div class="abs field" style="left:120px;top:2338px;width:229px">Email (required)</div>
<div class="abs field" style="left:358px;top:2338px;width:229px">Phone</div>
<div class="abs" style="left:120px;top:2398px;width:11px;height:11px;background:var(--white);border-radius:2px"></div>
<div class="abs" style="left:139px;top:2395px;font-size:13px;color:var(--muted)">Sign up for news and updates</div>
<div class="abs btn" style="left:123px;top:2439px;width:145px;height:43px;border:2px solid var(--yellow);color:var(--white)">Submit</div>

<!-- footer -->
<div class="abs footer-bg"></div>
<section class="abs cta">
  <div class="abs cta-tint"></div>
  <h2 class="abs serif cta-title">What does it<br>mean for you?</h2>
  <div class="abs btn" style="left:634px;top:58px;width:146px;height:43px;background:var(--ink);color:var(--white)">Contact Me</div>
</section>

<div class="abs logo" style="left:85px;top:2780px">Daniel Marrow</div>
<div class="abs" style="left:85px;top:2848px;font-size:14px;color:var(--muted)">Subscribe for updates</div>
<div class="abs" style="left:85px;top:2892px;width:272px;height:44px;border:1px solid #6a6a6a;border-radius:24px"></div>
<div class="abs" style="left:98px;top:2905px;font-size:13px;color:#cfcfcf">Your email address</div>
<svg class="abs" style="left:314px;top:2897px" width="36" height="36" viewBox="0 0 36 36"><circle cx="18" cy="18" r="18" fill="#f5bd00"/><path d="M10 18h15M19 12l6 6-6 6" fill="none" stroke="#141414" stroke-width="2.5" stroke-linecap="round" stroke-linejoin="round"/></svg>

<div class="abs col-head" style="left:741px;top:2797px">Quick Links</div>
<div class="abs col-link" style="left:741px;top:2846px">Home</div>
<div class="abs col-link" style="left:741px;top:2878px">Specialties</div>
<div class="abs col-link" style="left:741px;top:2910px">Contact Me</div>

<div class="abs col-head" style="left:949px;top:2797px">Specialties</div>
<div class="abs col-link" style="left:949px;top:2846px">Estate planning</div>
<div class="abs col-link" style="left:949px;top:2878px">Retirement forecasting</div>
<div class="abs col-link" style="left:949px;top:2910px">Final expense</div>
<div class="abs col-link" style="left:949px;top:2942px">Life insurance</div>
<div class="abs col-link" style="left:949px;top:2974px">Portfolio evaluation</div>

<div class="abs divider" style="top:3048px;background:#444"></div>
<div class="abs" style="left:85px;top:3078px;width:19px;height:19px;border:2px solid var(--white);border-radius:4px"></div>
<div class="abs" style="left:120px;top:3078px;width:19px;height:19px;background:var(--white);border-radius:3px"></div>
<div class="abs" style="left:154px;top:3080px;font-size:13px;color:var(--muted)">© 2024 <b style="color:var(--yellow)">Daniel Marrow</b> All right reserved</div>

</body>
</html>
```